Mechanical Engineer Business Card Design (Unemployed)

I am unemployed and actively looking for a job in Canada. I will be using this business card when I meet potential employers or in networking events.I would love to have the engraved writing style (as if it is engraved on the card). Some examples attached.I would love to have a personalized logo that represents my 2 majors. The final design should have a professional look that can stand out if attached to a resume. Jobs I am applying for are in construction, mining, oil and gas, Aerospace, manufacturing and whatever field I can be integrated in.A metallic look on the back is ok. but the front have to be sort of can be written on. you can also try to add my profilelink profile https://ca.profilelink.example/in/tomasvelder
On the front or back, I would love to have the symbol of mail and phone rather than the words. that saves spaceAmaze me guys.

Target Market(s)

Engineering

Industry/Entity Type

Engineering

Contact Information for Business Card

Tomas Velder
Mechanical Engineer

Phone number: +1 (555) 014 - 2738
email: veldertomas@mailbox.example

Requirements
Must have
• PERSONALIZED and brand new Simple Logo
• Professional look
• Engraved writing for the name
• Help stand out when attached on CV
Nice to have
• Metallic back look

```html
<!DOCTYPE html>
<html lang="en">
<head>
<meta charset="utf-8">
<title>Tomas Velder — Business Card</title>
<link rel="stylesheet" href="https://fonts.googleapis.com/css2?family=Montserrat:wght@700&family=Quicksand:wght@400;500&family=Michroma&display=swap">
<style>
  :root {
    --canvas: #e4e2de;
    --card-front: #f1efeb;
    --ink-dark: #1f2326;
    --ink-slate: #5d7284;
    --mark-slate: #2e4453;
    --carbon-dark: #111315;
    --carbon-mid: #23272b;
    --silver: #c9cbcd;
    --silver-deep: #8d9196;
  }
  * { margin: 0; padding: 0; box-sizing: border-box; }
  html, body { width: 1200px; height: 848px; overflow: hidden; }
  body {
    background: var(--canvas);
    position: relative;
    font-family: "Quicksand", sans-serif;
  }
  .card {
    position: absolute;
    top: 275px;
    width: 520px;
    height: 298px;
    border-radius: 24px;
    overflow: hidden;
    box-shadow: 0 10px 28px rgba(0,0,0,0.18);
  }
  /* Front */
  .card-front { left: 50px; background: var(--card-front); }
  .front-identity { position: absolute; left: 230px; top: 52px; }
  .front-name {
    font-family: "Montserrat", sans-serif;
    font-weight: 700;
    font-size: 19px;
    letter-spacing: 2.5px;
    color: var(--ink-dark);
    text-transform: uppercase;
  }
  .front-title {
    font-size: 13px;
    font-weight: 500;
    color: var(--ink-slate);
    margin-top: 2px;
    margin-left: 14px;
  }
  .contact-list { list-style: none; position: absolute; left: 200px; top: 124px; }
  .contact-item {
    display: flex; align-items: center; gap: 10px;
    font-size: 13px; font-weight: 500; color: var(--ink-dark);
    height: 26px;
  }
  .contact-icon { width: 18px; height: 18px; flex: none; }
  .profile-square { width: 14px; height: 14px; background: #2f78a8; border-radius: 2px; margin: 0 2px; flex: none; }
  .front-mark {
    position: absolute; left: 40px; top: 196px;
    display: flex; align-items: center; gap: 10px;
  }
  .mark-circle { width: 30px; height: 30px; border-radius: 50%; background: var(--mark-slate); }
  .front-mark .mark-name {
    font-family: "Montserrat", sans-serif; font-weight: 700;
    font-size: 20px; color: var(--mark-slate);
  }
  /* Back */
  .card-back { left: 630px; }
  .carbon-surface {
    position: absolute; inset: 0;
    background: radial-gradient(ellipse at 50% 40%, var(--carbon-mid), var(--carbon-dark) 75%);
  }
  .back-mark {
    position: absolute; left: 0; right: 0; top: 74px;
    display: flex; justify-content: center; align-items: center; gap: 12px;
  }
  .back-mark .mark-circle { background: var(--silver); width: 34px; height: 34px; }
  .back-mark .mark-name {
    font-family: "Montserrat", sans-serif; font-weight: 700;
    font-size: 24px; color: var(--silver);
  }
  .back-name {
    position: absolute; left: 0; right: 0; top: 178px;
    text-align: center;
    font-family: "Michroma", sans-serif;
    font-size: 24px; letter-spacing: 6px;
    text-transform: uppercase;
    color: var(--silver-deep);
    text-shadow: 0 1px 0 rgba(255,255,255,0.35), 0 -1px 0 rgba(0,0,0,0.9);
  }
</style>
</head>
<body>
  <section class="card card-front" aria-label="Card front">
    <div class="front-identity">
      <h1 class="front-name">Tomas Velder</h1>
      <p class="front-title">Mechanical engineer</p>
    </div>
    <ul class="contact-list">
      <li class="contact-item">
        <svg class="contact-icon" viewBox="0 0 18 18" aria-hidden="true"><rect x="4.5" y="1.5" width="9" height="15" rx="1.5" fill="none" stroke="#3b4248" stroke-width="1.5"/><line x1="7.5" y1="14" x2="10.5" y2="14" stroke="#3b4248" stroke-width="1.2"/></svg>
        <span>+1 (555) 014 - 2738</span>
      </li>
      <li class="contact-item">
        <svg class="contact-icon" viewBox="0 0 18 18" aria-hidden="true"><rect x="1.5" y="4" width="15" height="10" fill="#3b4248"/><polyline points="1.5,4 9,10 16.5,4" fill="none" stroke="#f1efeb" stroke-width="1.2"/></svg>
        <span>veldertomas@mailbox.example</span>
      </li>
      <li class="contact-item">
        <span class="profile-square" aria-hidden="true"></span>
        <span>ca.profilelink.example/in/tomasvelder</span>
      </li>
    </ul>
    <div class="front-mark">
      <span class="mark-circle" aria-hidden="true"></span>
      <span class="mark-name">Tomas Velder</span>
    </div>
  </section>

  <section class="card card-back" aria-label="Card back">
    <div class="carbon-surface" role="img" aria-label="Dark woven carbon-fibre texture"></div>
    <div class="back-mark">
      <span class="mark-circle" aria-hidden="true"></span>
      <span class="mark-name">Tomas Velder</span>
    </div>
    <p class="back-name">Tomas Velder</p>
  </section>
</body>
</html>
```